design a construction company business card

Design business card around our logo. Card must have all the typical info: name, title, address, phone, email, business name, etc. Somewhere on the card I would like to see our motto "Built with purpose... Driven by dedication." Consider adding a splash of bright orange to the card to complement the blues and silvers/grays in the logo. We are open to metallic inks, textures, etc. We would like to see options on both light and dark backgrounds. The font in the logo is Euro Technic Extended Regular.

```html
<!DOCTYPE html>
<html lang="en">
<head>
<meta charset="utf-8">
<title>Halden Contracting, Inc. – Business Cards</title>
<link rel="stylesheet" href="https://fonts.googleapis.com/css2?family=Michroma&family=Saira:wdth,wght@75..125,100..900&display=swap">
<style>
  :root {
    --stage-light: #c9c9c9;
    --stage-dark: #a4a4a4;
    --navy: #21409a;
    --blue: #1f6ab7;
    --blue-deep: #223f95;
    --silver: #d9dde2;
    --slate: #8d939b;
    --orange: #f7941e;
    --white: #ffffff;
    --card-light: #f4f5f6;
  }
  * { box-sizing: border-box; margin: 0; padding: 0; }
  html, body { width: 1000px; height: 1200px; overflow: hidden; }
  body {
    position: relative;
    background: radial-gradient(ellipse at 50% 45%, var(--stage-light) 0%, var(--stage-dark) 100%);
    font-family: "Saira", sans-serif;
  }
  .card {
    position: absolute;
    left: 201px;
    width: 577px;
    height: 329px;
    box-shadow: 0 6px 14px rgba(0,0,0,0.25);
  }

  /* Front (dark) */
  .card--front {
    top: 167px;
    background: radial-gradient(ellipse at 50% 30%, #2a7ac6 0%, var(--blue) 35%, var(--blue-deep) 100%);
  }
  .front-brand {
    position: absolute;
    left: 0; right: 0; top: 168px;
    text-align: center;
    font-family: "Michroma", sans-serif;
    color: var(--silver);
  }
  .front-brand__name { font-size: 52px; letter-spacing: 4px; line-height: 1; }
  .front-brand__sub { margin-top: 14px; font-size: 16px; letter-spacing: 1px; }

  /* Back (light) */
  .card--back {
    top: 697px;
    background: radial-gradient(ellipse at 55% 20%, var(--white) 0%, var(--card-light) 55%, #dcdfe2 100%);
  }
  .back-brand {
    position: absolute;
    left: 21px; top: 92px;
    width: 200px;
    text-align: center;
    font-family: "Michroma", sans-serif;
    color: var(--navy);
  }
  .back-brand__name { font-size: 30px; letter-spacing: 2px; line-height: 1; }
  .back-brand__sub { margin-top: 7px; font-size: 9.5px; letter-spacing: 0.5px; }

  .holder {
    position: absolute;
    right: 23px; top: 33px;
    text-align: right;
  }
  .holder__name {
    font-size: 19px;
    font-weight: 700;
    font-stretch: 125%;
    letter-spacing: 0.5px;
    line-height: 1.1;
    color: var(--navy);
  }
  .holder__name .surname { color: var(--orange); }
  .holder__title { font-size: 16px; color: var(--blue); line-height: 1.2; }

  .motto {
    position: absolute;
    left: 20px; top: 183px;
    width: 534px; height: 24px;
    background: var(--orange);
    color: var(--white);
    font-size: 15px;
    font-weight: 700;
    font-stretch: 125%;
    letter-spacing: 1.2px;
    line-height: 24px;
    padding-left: 9px;
    white-space: nowrap;
    overflow: hidden;
  }
  .contact-band {
    position: absolute;
    left: 20px; top: 212px;
    width: 534px; height: 95px;
    background: linear-gradient(180deg, var(--blue) 0%, var(--blue-deep) 100%);
    color: var(--white);
    font-size: 14.5px;
    font-stretch: 110%;
  }
  .contact-list { position: absolute; left: 11px; top: 14px; list-style: none; }
  .contact-list li { display: flex; align-items: center; height: 23px; }
  .contact-list svg { width: 14px; height: 14px; margin-right: 10px; flex: none; }
  .address { position: absolute; left: 342px; top: 14px; }
  .address svg { position: absolute; left: 0; top: 3px; width: 12px; height: 16px; }
  .address p { margin-left: 20px; line-height: 23px; white-space: nowrap; }
</style>
</head>
<body>

<section class="card card--front" aria-label="Business card front">
  <div class="front-brand">
    <div class="front-brand__name">HALDEN</div>
    <div class="front-brand__sub">CONTRACTING, INC.</div>
  </div>
</section>

<section class="card card--back" aria-label="Business card back">
  <div class="back-brand">
    <div class="back-brand__name">HALDEN</div>
    <div class="back-brand__sub">CONTRACTING, INC.</div>
  </div>

  <div class="holder">
    <div class="holder__name">DAN <span class="surname">HALDEN</span></div>
    <div class="holder__title">President</div>
  </div>

  <div class="motto">Built with purpose... Driven by dedication.</div>

  <div class="contact-band">
    <ul class="contact-list">
      <li>
        <svg viewBox="0 0 14 14" aria-hidden="true"><rect x="3" y="0.5" width="8" height="13" rx="1.5" fill="var(--orange)"/><rect x="4.5" y="2" width="5" height="8" fill="var(--blue)"/><circle cx="7" cy="11.7" r="0.9" fill="var(--blue)"/></svg>
        (555) 204-7781
      </li>
      <li>
        <svg viewBox="0 0 14 14" aria-hidden="true"><rect x="0.5" y="2.5" width="13" height="9" fill="var(--orange)"/><path d="M0.8 2.8 L7 8 L13.2 2.8" fill="none" stroke="var(--blue)" stroke-width="1.2"/></svg>
        info@haldencontracting.com
      </li>
      <li>
        <svg viewBox="0 0 14 14" aria-hidden="true"><circle cx="7" cy="7" r="6.5" fill="var(--orange)"/><path d="M3 4 Q5 3 6 5 T5 9 L4 11 M8 2 Q9 5 11 5 M9 9 Q10 11 12 9" fill="none" stroke="var(--blue)" stroke-width="1.3"/></svg>
        haldencontracting.example.com
      </li>
    </ul>
    <div class="address">
      <svg viewBox="0 0 12 16" aria-hidden="true"><path d="M6 0.5 A5.5 5.5 0 0 1 11.5 6 C11.5 10 6 15.5 6 15.5 C6 15.5 0.5 10 0.5 6 A5.5 5.5 0 0 1 6 0.5 Z" fill="var(--orange)"/><circle cx="6" cy="6" r="2" fill="var(--blue)"/></svg>
      <p>Halden Contracting, Inc.</p>
      <p>2740 Larkspur Avenue</p>
      <p>Fairview, OH 45099</p>
    </div>
  </div>
</section>

</body>
</html>
```